Ridgely Forge business card for handing simple contact information and generating service awareness

Utilizing the attached logo(s), generate a professional, but approachable, card conveying a sense of capability and integrity. Please only use one logo of the four attached; the different colors are all acceptable, but preference will be given to a design integrating a teal/turquoise logo,

I do not know where to put in the contact information or details?

Target Market(s)

Agriculture, Farming, Timber, Forestry, Construction, Crane Service

Industry/Entity Type

Contact Information for Business Card

Name, Phone Number, email address

Colors

Designer to choose colors to be used in the design.

Requirements
Nice to have
• It would be great to have either a mountain or one of the attached cranes as a backdrop on the rear of the card. Simple watermarks and/or Debossing is also great

```html
<!DOCTYPE html>
<html lang="en">
<head>
<meta charset="UTF-8">
<title>Ridgely Forge — Business Card</title>
<link href="https://fonts.googleapis.com/css2?family=Montserrat:wght@400;500;800&display=swap" rel="stylesheet">
<style>
  :root {
    --backdrop: #141414;
    --card-dark: #1f1f1f;
    --card-light: #2e2e2e;
    --teal: #2f8f7c;
    --ink: #f2f2f2;
  }
  * { box-sizing: border-box; margin: 0; padding: 0; }
  html, body {
    width: 1200px; height: 900px; overflow: hidden;
    background: var(--backdrop);
    font-family: "Montserrat", sans-serif;
  }
  .sheet {
    width: 1200px; height: 900px;
    display: flex; flex-direction: column; align-items: center; justify-content: center;
    gap: 30px;
  }
  .card {
    width: 700px; height: 400px;
    background: linear-gradient(135deg, var(--card-dark) 0%, var(--card-dark) 45%, var(--card-light) 100%);
    position: relative;
  }
  .brand {
    display: flex; align-items: center; gap: 14px;
    color: var(--teal); font-weight: 800; text-transform: uppercase;
    letter-spacing: 1px;
  }
  .brand-dot {
    border-radius: 50%; background: var(--teal); flex: none;
  }
  .card-front { display: flex; align-items: center; justify-content: center; }
  .card-front .brand { font-size: 44px; }
  .card-front .brand-dot { width: 40px; height: 40px; }

  .card-back { display: flex; align-items: center; }
  .back-brand {
    width: 340px; display: flex; justify-content: center;
  }
  .card-back .brand { font-size: 26px; gap: 10px; }
  .card-back .brand-dot { width: 26px; height: 26px; }
  .divider {
    width: 2px; height: 250px; background: var(--teal);
  }
  .contact { padding-left: 38px; color: var(--ink); }
  .person-name {
    color: var(--teal); font-weight: 800; font-size: 30px;
    letter-spacing: 2px; text-transform: uppercase; line-height: 1;
  }
  .person-role {
    font-size: 15px; letter-spacing: 1.5px; text-transform: uppercase;
    margin-top: 6px; font-weight: 500;
  }
  .address { font-size: 15px; line-height: 1.35; margin-top: 26px; letter-spacing: .4px; }
  .lines { list-style: none; margin-top: 24px; }
  .lines li {
    display: flex; align-items: center; gap: 12px;
    font-size: 16px; letter-spacing: .4px; margin-bottom: 9px;
  }
  .lines svg { width: 16px; height: 16px; flex: none; }
</style>
</head>
<body>
<main class="sheet">
  <section class="card card-front">
    <div class="brand"><span class="brand-dot"></span>Ridgely Forge</div>
  </section>

  <section class="card card-back">
    <div class="back-brand">
      <div class="brand"><span class="brand-dot"></span>Ridgely Forge</div>
    </div>
    <div class="divider"></div>
    <div class="contact">
      <h1 class="person-name">Dana Keller</h1>
      <p class="person-role">Manager</p>
      <p class="address">482 North Pine Hollow Road 12<br>Cedar Falls, MN 55807</p>
      <ul class="lines">
        <li>
          <svg viewBox="0 0 24 24" aria-hidden="true"><path fill="#2f8f7c" d="M6.6 10.8a15.1 15.1 0 0 0 6.6 6.6l2.2-2.2a1 1 0 0 1 1-.25 11.4 11.4 0 0 0 3.6.57 1 1 0 0 1 1 1V20a1 1 0 0 1-1 1A17 17 0 0 1 3 4a1 1 0 0 1 1-1h3.5a1 1 0 0 1 1 1c0 1.25.2 2.45.57 3.57a1 1 0 0 1-.25 1z"/></svg>
          (218)555-0147
        </li>
        <li>
          <svg viewBox="0 0 24 24" aria-hidden="true"><rect x="2" y="5" width="20" height="14" rx="1.5" fill="#2f8f7c"/><path d="M3 6l9 7 9-7" fill="none" stroke="#1f1f1f" stroke-width="1.6"/></svg>
          office@ridgelyforge.com
        </li>
        <li>
          <svg viewBox="0 0 24 24" aria-hidden="true"><g fill="none" stroke="#2f8f7c" stroke-width="1.8"><circle cx="12" cy="12" r="9"/><ellipse cx="12" cy="12" rx="4" ry="9"/><path d="M3 12h18M4.5 7.5h15M4.5 16.5h15"/></g></svg>
          www.ridgelyforge.com
        </li>
      </ul>
    </div>
  </section>
</main>
</body>
</html>
```